Steadfast Voyage Partners Capability Statement

Steadfast Voyage Partners is a Corporate Travel Management company based in Brisbane, Australia. Please review our 'About Us' page of our website to gain an understanding of our company culture (www.steadfastvoyagepartners.example.com.au). We are extremely customer focused. We see ourselves as an extension of our client's business.We require a powerful 1 page infographic that highlights what we do - 'Capability Statement' to use as an initial introduction to prospect clients when they ask for information about us.* Our Core Competencies - Service / People / Technology (this is our tagline so I think the document should follow this format)* A Company snapshot - Office location and website (needs to be editable to add Licence information)* Performance / Key Benefits (needs to editable to add in testimonials and case studies)* Client retention result 96%* Employee retention 98%* Affiliations & Partnerships (we will add)*Awards (see details to include)* Contact Details (at the bottom of the page - Marcus Van Heerden marcus@svpartners.example.com.au+61 448 187 226Differentiators (for us to complete so doc must be editable)The format of the document needs to be easily modified when required. I have attached the company logos and branding colours / font etc. Thank youRegardsMiriam

Target Market(s)

Medium businesses Australian based

Industry/Entity Type

Travel Industry

Font styles to use
Sans Serif

Colors
abd036

Requirements
Must have
• Content Outlined and corporate colours. Must be easily editable.

```html
<!DOCTYPE html>
<html lang="en">
<head>
<meta charset="utf-8">
<title>Steadfast Voyage Partners – Capability Statement</title>
<link href="https://fonts.googleapis.com/css2?family=Exo+2:ital,wght@1,600;1,700&family=Source+Sans+3:ital,wght@0,400;0,600;0,700;1,400&display=swap" rel="stylesheet">
<style>
:root{
  --brand-green:#abd036;
  --column-green:#86c440;
  --pill-green:#c2d82e;
  --bar-grey:#6b6c6f;
  --footer-grey:#6b6c6f;
  --ink:#6a6a6a;
  --white:#ffffff;
  --pie-green:#c8df2a;
  --pie-edge:#9fb722;
}
*{box-sizing:border-box;margin:0;padding:0}
html,body{width:1046px;height:1200px;overflow:hidden;background:#fff}
body{font-family:"Source Sans 3",sans-serif;color:var(--ink)}
.sheet{position:relative;width:1046px;height:1200px;background:var(--white);overflow:hidden}

.hero-photo{position:absolute;left:0;top:0;width:1046px;height:268px;
  background:linear-gradient(180deg,#9c9ea0 0%,#b9bbbd 45%,#7d7f81 80%,#3e4042 100%)}
.hero-photo-right{position:absolute;left:500px;top:268px;width:546px;height:70px;
  background:linear-gradient(180deg,#404244 0%,#6b6d6f 100%)}

.brand{position:absolute;left:560px;top:44px;width:460px;display:flex;align-items:center;gap:14px}
.brand-mark{width:22px;height:22px;background:var(--brand-green);flex:none}
.brand-name{font-family:"Source Sans 3",sans-serif;font-weight:700;font-size:33px;line-height:1;color:var(--white);letter-spacing:-.3px}
.brand-tagline{position:absolute;left:600px;top:134px;width:416px;text-align:right;font-family:"Exo 2",sans-serif;font-style:italic;font-weight:600;font-size:19px;color:var(--brand-green);letter-spacing:.5px}
.doc-title{position:absolute;right:30px;top:192px;font-family:"Exo 2",sans-serif;font-style:italic;font-weight:700;font-size:34px;color:var(--brand-green);letter-spacing:.5px}
.doc-subtitle{position:absolute;right:30px;top:230px;font-family:"Exo 2",sans-serif;font-style:italic;font-weight:700;font-size:18px;color:var(--white)}

.left-column{position:absolute;left:0;top:268px;width:500px;height:777px;background:var(--column-green);color:var(--white)}
.pill{position:absolute;left:0;width:283px;height:32px;background:var(--pill-green);border-radius:0 16px 16px 0;
  font-weight:600;font-size:15px;line-height:32px;padding-left:30px;color:var(--white)}
.copy{position:absolute;left:30px;width:440px;font-size:13.2px;line-height:16.5px;text-align:justify}
.copy p+p{margin-top:11px}
.benefits{position:absolute;left:30px;top:477px;width:380px;list-style:none;font-size:13px;line-height:17px}
.benefits li{position:relative;padding-left:16px}
.benefits li::before{content:"";position:absolute;left:0;top:4px;width:9px;height:9px;border-radius:50%;background:var(--white)}
.benefits li::after{content:"";position:absolute;left:2.5px;top:6.5px;width:3px;height:3px;border-top:1.4px solid var(--column-green);border-right:1.4px solid var(--column-green);transform:rotate(45deg)}

.contact{position:absolute;left:0;top:1045px;width:500px;height:155px;background:var(--footer-grey);color:var(--white)}
.contact-item{position:absolute;left:30px;display:flex;align-items:center;gap:12px;font-size:15.5px}
.contact-icon{width:17px;height:17px;border-radius:50%;background:var(--brand-green);flex:none}
.licence{position:absolute;left:0;width:500px;top:126px;text-align:center;font-size:13px;color:var(--brand-green)}

.section-bar{position:absolute;left:500px;width:516px;height:22px;background:var(--bar-grey);color:var(--white);
  font-weight:600;font-size:15px;line-height:22px;padding-left:45px}

.services{position:absolute;left:519px;top:390px;width:498px;height:210px}
.service{position:absolute;width:166px;text-align:center;font-size:13px;color:var(--ink)}
.service svg{display:block;margin:0 auto 8px}
.divider-v{position:absolute;border-left:1.5px dotted #999}
.divider-h{position:absolute;border-top:1.5px dotted #999}

.award{position:absolute;top:655px;text-align:center;font-size:9px;letter-spacing:1px;color:#666}
.award-badge{width:74px;height:78px;background:linear-gradient(180deg,#b6cf55,#dfe9b7);border-radius:4px;margin:0 auto 4px}
.award-caption{border-top:1px solid #999;border-bottom:1px solid #999;padding:2px 0;width:80px}

.pie{position:absolute;top:813px;width:82px;text-align:center}
.pie-label{font-size:14.5px;line-height:19px;color:#777;margin-top:6px}
.testimonial{position:absolute;left:548px;top:953px;width:468px;font-style:italic;font-size:12.8px;line-height:17.5px;text-align:justify;color:#777}

.partners{position:absolute;left:536px;width:490px;display:flex;justify-content:space-between;align-items:center}
.partner{font-weight:700;font-size:16px;color:#2f3a8f}
.partner.small{font-size:12px}
</style>
</head>
<body>
<main class="sheet">

  <div class="hero-photo" role="img" aria-label="Black and white photograph of a jet aircraft taking off over a runway"></div>
  <div class="hero-photo-right" role="img" aria-label="Continuation of the runway photograph"></div>

  <div class="brand">
    <span class="brand-mark"></span>
    <span class="brand-name">Steadfast Voyage Partners</span>
  </div>
  <div class="brand-tagline">PEOPLE | SERVICE | TECHNOLOGY</div>
  <h1 class="doc-title">CAPABILITY STATEMENT</h1>
  <div class="doc-subtitle">Service / People / Technology</div>

  <section class="left-column">
    <div class="pill" style="top:31px">OUR MISSION</div>
    <div class="copy" style="top:80px">
      <p>We are a dynamic multi-award winning team of industry experts that deliver confidence and business travel certainty.</p>
    </div>

    <div class="pill" style="top:143px">COMPANY OVERVIEW</div>
    <div class="copy" style="top:188px">
      <p>Steadfast Voyage Partners was founded on the vision of delivering a superior customer experience and end to end business travel management solutions.</p>
      <p>Opening for business in 2005, SVP is a progressive business travel management company and corporate travel specialist.</p>
      <p>We focus on engaging industry-best consultants and market leading technology.</p>
      <p>Clients trust and appreciate the depth of experience and knowledge that exists within our team which provides them with travel assurance and ultimate value. Today, Steadfast Voyage Partners sustains an award-winning reputation for outstanding service.</p>
    </div>

    <div class="pill" style="top:429px">KEY BENEFITS</div>
    <ul class="benefits">
      <li>Dedicated customer focused team</li>
      <li>High touch, end to end service offering</li>
      <li>Industry experts with a minimum of 10 years experience</li>
      <li>Dedicated Account Management</li>
      <li>Dynamic Drill-Down Management Information Reporting</li>
      <li>Australian based 24/7 After Hours solution</li>
      <li>Global travel program management</li>
      <li>Market leading technology platforms</li>
      <li>Mobile App</li>
      <li>Duty of Care &amp; Risk Management solutions</li>
      <li>Tailored reporting solutions</li>
      <li>Reconciliation services</li>
      <li>Flexible payment solutions</li>
      <li>A member of Australia's largest buying group providing competitive air, hotel and car savings</li>
      <li>A Southern Cross Air platinum agent for 7 consecutive years</li>
      <li>Average client partnership &gt; 8 years</li>
    </ul>
  </section>

  <footer class="contact">
    <div class="contact-item" style="top:14px"><span class="contact-icon"></span>+61 455 903 618</div>
    <div class="contact-item" style="top:41px"><span class="contact-icon"></span>marcus@svpartners.example.com.au</div>
    <div class="contact-item" style="top:67px"><span class="contact-icon"></span>www.steadfastvoyagepartners.example.com.au</div>
    <div class="contact-item" style="top:94px"><span class="contact-icon"></span>48 Fernvale St Kelvin Ridge 4109</div>
    <div class="licence">ATRA Licence 04 51872 3</div>
  </footer>

  <h2 class="section-bar" style="top:361px">SERVICES OVERVIEW</h2>
  <div class="services">
    <div class="divider-v" style="left:163px;top:8px;height:185px"></div>
    <div class="divider-v" style="left:330px;top:8px;height:185px"></div>
    <div class="divider-h" style="left:0;top:98px;width:485px"></div>

    <div class="service" style="left:0;top:12px">
      <svg width="52" height="46" viewBox="0 0 52 46" fill="none" stroke="#9bc43a" stroke-width="1.6"><circle cx="26" cy="23" r="12"/><circle cx="26" cy="6" r="4"/><circle cx="8" cy="33" r="4"/><circle cx="44" cy="33" r="4"/><circle cx="26" cy="23" r="3"/></svg>PROCESS</div>
    <div class="service" style="left:166px;top:12px">
      <svg width="52" height="46" viewBox="0 0 52 46" fill="none" stroke="#9bc43a" stroke-width="1.8"><circle cx="24" cy="23" r="19"/><circle cx="28" cy="23" r="19"/><text x="19" y="31" font-size="22" fill="#9bc43a" stroke="none" font-family="sans-serif">$</text></svg>SAVINGS</div>
    <div class="service" style="left:332px;top:12px">
      <svg width="52" height="46" viewBox="0 0 52 46" fill="none" stroke="#9bc43a" stroke-width="1.6"><path d="M12 2h20l8 8v32H12z"/><path d="M17 14h16M17 20h16M17 26h12"/><circle cx="40" cy="35" r="6"/><path d="M37 35l2 2 4-4"/></svg>CONTROL</div>
    <div class="service" style="left:0;top:110px">
      <svg width="52" height="46" viewBox="0 0 52 46" fill="none" stroke="#9bc43a" stroke-width="1.6"><rect x="6" y="6" width="32" height="22"/><path d="M18 34h10M22 28v6"/><rect x="32" y="16" width="12" height="22" rx="2"/></svg>MOBILE</div>
    <div class="service" style="left:166px;top:110px">
      <svg width="52" height="46" viewBox="0 0 52 46" fill="none" stroke="#9bc43a" stroke-width="1.6"><rect x="13" y="4" width="24" height="38"/><circle cx="21" cy="14" r="4"/><path d="M18 24h14M18 30h14M18 36h10"/></svg>POLICY</div>
    <div class="service" style="left:332px;top:110px">
      <svg width="52" height="46" viewBox="0 0 52 46" fill="none" stroke="#9bc43a" stroke-width="1.6"><path d="M8 4v36h38"/><path d="M12 34l8-10 7 6 8-12 8 6"/></svg>VISIBILITY</div>
  </div>

  <h2 class="section-bar" style="top:610px">INDUSTRY ACHIEVEMENTS</h2>
  <div class="award" style="left:548px"><div class="award-badge"></div><div class="award-caption">FINALIST 2018</div></div>
  <div class="award" style="left:636px"><div class="award-badge"></div><div class="award-caption">FINALIST 2017</div></div>
  <div class="award" style="left:770px"><div class="award-badge"></div><div class="award-caption">WINNER 2015</div></div>

  <h2 class="section-bar" style="top:784px">SERVICE / PEOPLE / TECHNOLOGY</h2>
  <div class="pie" style="left:549px">
    <svg width="82" height="82" viewBox="0 0 82 82"><circle cx="41" cy="41" r="38" fill="var(--pie-green)" stroke="var(--pie-edge)" stroke-width="1.5"/><path d="M41 41L41 3A38 38 0 0 1 50.45 4.2Z" fill="#fff"/><text x="41" y="45" text-anchor="middle" font-size="11" fill="#6b8a12" font-family="Source Sans 3, sans-serif">96%</text></svg>
    <div class="pie-label">Client<br>Retention</div>
  </div>
  <div class="pie" style="left:707px">
    <svg width="82" height="82" viewBox="0 0 82 82"><circle cx="41" cy="41" r="38" fill="var(--pie-green)" stroke="var(--pie-edge)" stroke-width="1.5"/><path d="M41 41L41 3A38 38 0 0 1 45.76 3.3Z" fill="#fff"/><text x="41" y="45" text-anchor="middle" font-size="11" fill="#6b8a12" font-family="Source Sans 3, sans-serif">98%</text></svg>
    <div class="pie-label">Employee<br>Retention</div>
  </div>
  <p class="testimonial">"SVP has been a very supportive and innovative Travel Management Company for our organisation. Oliver and his team of consultants has been servicing Halden Property Group for more than 6 years providing a range of travel and financial account support to our business." Halden Property Group</p>

  <h2 class="section-bar" style="top:1048px">AFFILIATIONS &amp; PARTNERSHIPS</h2>
  <div class="partners" style="top:1106px">
    <span class="partner">Harbourline</span>
    <span class="partner">Tessly</span>
    <span class="partner">Summit Circle</span>
    <span class="partner">Orbitline</span>
  </div>
  <div class="partners" style="top:1144px">
    <span class="partner">Gatewise</span>
    <span class="partner">Farebridge</span>
    <span class="partner small">Routecraft</span>
    <span class="partner small">NTAA</span>
    <span class="partner small">TAAS</span>
    <span class="partner small">ATRA</span>
  </div>

</main>
</body>
</html>
```